Thermal Camera flyer

We would like to obtain a sales orientated brochure to promote our two models of thermal imaging cameras as a response to the current Covid 19 health issues. I have provided the text, photos and detailed product specifications , in addition to a sample competitors brochure.
BROCHURE Details : 2 sided - front side to show product, its applications in business, school, hospitals, with text details - Back page to show specifications chart and contact information for Corvel Signal Works. (Melbourne -Sydney-Perth-Brisbane - 1300 647 519
Brochure should be "eye-catching" and reflect the product as a high quality, must-have technology device for todays world.

```html
<!DOCTYPE html>
<html lang="en">
<head>
<meta charset="utf-8">
<title>Thermal Scanning and Facial Recognition Camera – Corvel Signal Works</title>
<link href="https://fonts.googleapis.com/css2?family=Krona+One&family=Roboto+Slab:wght@800&family=Arimo:wght@400;700&display=swap" rel="stylesheet">
<style>
  :root {
    --ink: #141416;
    --magenta: #c2185b;
    --magenta-soft: #a8124e;
    --white: #f4f4f6;
    --grey: #b9b9c0;
    --ring: #d9d9de;
    --brand-blue: #2e6fd8;
  }
  * { margin: 0; padding: 0; box-sizing: border-box; }
  html, body { width: 1200px; height: 862px; overflow: hidden; background: #2a2a2e; }
  .flyer {
    position: relative; width: 1200px; height: 862px; overflow: hidden;
    background: radial-gradient(ellipse at 70% 40%, #26262b 0%, var(--ink) 70%);
    font-family: "Arimo", Arial, sans-serif; color: var(--white);
  }
  .backdrop { position: absolute; inset: 0; }
  .title {
    position: absolute; left: 60px; top: 100px; width: 420px;
    font-family: "Krona One", sans-serif; font-size: 31px; line-height: 1.28;
    color: var(--magenta); text-transform: uppercase; letter-spacing: 0.5px; font-weight: 400;
  }
  .purpose {
    position: absolute; left: 70px; top: 345px; width: 370px;
    border-left: 5px solid var(--magenta-soft); padding-left: 16px;
  }
  .purpose h2 {
    font-family: "Roboto Slab", serif; font-weight: 800; font-size: 18px;
    line-height: 1.18; text-transform: uppercase; margin-bottom: 14px; color: var(--white);
  }
  .purpose p { font-size: 12.5px; line-height: 1.55; color: var(--grey); margin-bottom: 10px; }
  .brand { position: absolute; left: 90px; top: 720px; display: flex; align-items: flex-start; gap: 12px; }
  .brand-mark { width: 30px; height: 30px; background: var(--brand-blue); margin-top: 4px; }
  .brand-name { font-size: 21px; color: var(--brand-blue); line-height: 1; }
  .brand-meta { font-size: 9.5px; letter-spacing: 2px; color: var(--grey); margin-top: 6px; line-height: 1.6; text-transform: uppercase; }
  .product-label {
    position: absolute; font-weight: 700; font-size: 15px;
    text-transform: uppercase; letter-spacing: 1px; line-height: 1.25;
  }
  .label-floor { left: 915px; top: 130px; }
  .label-desk { left: 700px; top: 562px; }
  .label-sub { color: var(--grey); font-weight: 400; }
  .cta { position: absolute; right: 70px; top: 690px; text-align: right; }
  .cta-phone { font-family: "Krona One", sans-serif; font-size: 38px; color: var(--magenta); }
  .cta-note { font-family: "Roboto Slab", serif; font-weight: 800; font-size: 13px; letter-spacing: 1.5px; text-transform: uppercase; margin-top: 6px; }
  .cta-web { font-size: 18px; letter-spacing: 5px; color: var(--magenta-soft); margin-top: 6px; }
</style>
</head>
<body>
<main class="flyer">
  <svg class="backdrop" width="1200" height="862" viewBox="0 0 1200 862" aria-hidden="true">
    <defs>
      <radialGradient id="showcaseGlow" cx="45%" cy="55%" r="65%">
        <stop offset="0%" stop-color="#2a3fc9"/>
        <stop offset="45%" stop-color="#3b1e8f"/>
        <stop offset="80%" stop-color="#5a1a8c"/>
        <stop offset="100%" stop-color="#8a1a6c"/>
      </radialGradient>
      <linearGradient id="unitTone" x1="0" y1="0" x2="0" y2="1">
        <stop offset="0%" stop-color="#d6d8de"/>
        <stop offset="55%" stop-color="#7d8190"/>
        <stop offset="100%" stop-color="#18181c"/>
      </linearGradient>
    </defs>
    <circle cx="800" cy="330" r="400" fill="#1a1a1d"/>
    <circle cx="800" cy="320" r="345" fill="none" stroke="var(--ring)" stroke-width="8"/>
    <circle cx="800" cy="320" r="338" fill="#0f0f11"/>
    <circle cx="800" cy="300" r="320" fill="url(#showcaseGlow)" role="img" aria-label="Glowing purple and blue backdrop with light streaks"/>
  </svg>

  <svg class="backdrop" width="1200" height="862" viewBox="0 0 1200 862">
    <rect class="product-photo photo-floor" x="830" y="40" width="75" height="480" rx="10" fill="url(#unitTone)" opacity="0.85" role="img" aria-label="Photo of the portable floor standing thermal camera on a tall pole"/>
    <rect class="product-photo photo-desk" x="560" y="120" width="200" height="420" rx="14" fill="url(#unitTone)" opacity="0.9" role="img" aria-label="Photo of the portable reception desk thermal camera on a low base"/>
  </svg>

  <h1 class="title">Thermal Scanning<br>and Facial<br>Recognition<br>Camera</h1>

  <section class="purpose">
    <h2>The Purpose of<br>Thermal Scanning<br>&amp; Facial Recognition</h2>
    <p>The purpose is to identify anyone walking into an establishment with a high temperature. This will reduce the likelihood of spreading any potential virus and brings some peace of mind to people in the building.</p>
    <p>We can pair your thermal camera/s with facial recognition software. Employees will check in by standing in front of the camera, which identifies them by their face in just a few seconds without contact (with or without a mask on) and simultaneously performs a thermal scan. It will record a photo of the individual, the date, the time and the temperature reading at that time of entering the building. If the camera detects a high temperature reading, it will sound an alarm in real time and send a notification to a nominated administrator/in-house security.</p>
  </section>

  <div class="brand">
    <span class="brand-mark"></span>
    <div>
      <div class="brand-name">Corvel Signal Works</div>
      <div class="brand-meta">Melbourne-Sydney-Perth-Brisbane<br>1300 647 519</div>
    </div>
  </div>

  <div class="product-label label-floor">Portable Floor<br><span class="label-sub">Standing Camera</span></div>
  <div class="product-label label-desk">Portable Camera<br><span class="label-sub">For Recepton Desk</span></div>

  <div class="cta">
    <div class="cta-phone">CALL 1300 647 519</div>
    <div class="cta-note">For further information and a free quote</div>
    <div class="cta-web">www.corvelsignal.com.au</div>
  </div>
</main>
</body>
</html>
```